Business card design for Plumbing and Gas fitting company

We need a business card design for our plumbing and gas fitting company using the company logo and director details. Design should be modern and eye-catching however kept reasonably simple. This design should be targeted at commercial businesses/work so professionalism is key.

Target Market(s)

Commercial/business

Industry/Entity Type

Plumbing

Contact Information for Business Card

Warwick Tane
Director
027 815 0937
warwick@harbourlinepipeworks.example
PO Box 8716
Palmerston North 4441

Font styles to use
Sans Serif

Requirements
Must have
• Logo
• Modern
• Kept simple
Nice to have
• Colour scheme based around logo

```html
<!DOCTYPE html>
<html lang="en">
<head>
<meta charset="utf-8">
<title>Harbourline Pipeworks – Business Card</title>
<link rel="stylesheet" href="https://fonts.googleapis.com/css2?family=Open+Sans:ital,wght@0,400;0,600;0,700;1,400&display=swap">
<style>
  :root {
    --brand-blue: #0f72bd;
    --accent-orange: #e8782f;
    --ink-grey: #555a5f;
    --card-white: #ffffff;
    --page-bg: #e9e7e3;
    --shadow: rgba(0, 0, 0, 0.18);
  }
  * { box-sizing: border-box; margin: 0; padding: 0; }
  html, body {
    width: 1200px;
    height: 987px;
    overflow: hidden;
    background: var(--page-bg);
    font-family: "Open Sans", Arial, sans-serif;
  }
  .card {
    position: absolute;
    left: 293px;
    width: 615px;
    height: 350px;
    box-shadow: 0 3px 10px var(--shadow);
  }
  .card--front { top: 130px; background: var(--card-white); }
  .card--back  { top: 506px; background: var(--brand-blue); }

  .brand {
    position: absolute;
    display: flex;
    align-items: center;
    gap: 10px;
    font-weight: 700;
    white-space: nowrap;
  }
  .brand__dot {
    width: 14px;
    height: 14px;
    border-radius: 50%;
  }
  .card--front .brand {
    left: 41px;
    top: 58px;
    font-size: 26px;
    color: var(--brand-blue);
  }
  .card--front .brand__dot { background: var(--brand-blue); }

  .contact {
    position: absolute;
    left: 41px;
    top: 196px;
    color: var(--ink-grey);
    font-size: 15px;
    line-height: 23px;
    list-style: none;
  }
  .contact__address { margin-bottom: 4px; }
  .contact__item {
    display: flex;
    align-items: center;
    gap: 8px;
    height: 24px;
  }
  .contact__icon { width: 14px; height: 14px; flex: none; }

  .person {
    position: absolute;
    right: 41px;
    top: 233px;
    text-align: right;
  }
  .person__name {
    font-size: 20px;
    font-weight: 600;
    color: var(--brand-blue);
    line-height: 28px;
  }
  .person__role {
    font-size: 15px;
    color: var(--accent-orange);
    line-height: 20px;
  }

  .card--back .brand {
    left: 0;
    right: 0;
    top: 148px;
    justify-content: center;
    font-size: 36px;
    color: var(--card-white);
  }
  .card--back .brand__dot { background: var(--card-white); width: 18px; height: 18px; }
  .web {
    position: absolute;
    left: 0;
    right: 0;
    top: 283px;
    text-align: center;
    color: var(--card-white);
    font-size: 15px;
    font-style: italic;
    letter-spacing: 1.6px;
  }
</style>
</head>
<body>
  <section class="card card--front" aria-label="Business card front">
    <div class="brand"><span class="brand__dot"></span>Harbourline Pipeworks</div>

    <ul class="contact">
      <li class="contact__address">PO Box 8716<br>Palmerston North 4441</li>
      <li class="contact__item">
        <svg class="contact__icon" viewBox="0 0 16 16" aria-hidden="true"><path fill="#0f72bd" d="M3.6 1.2 5.8 3.4c.4.4.4 1 0 1.4L4.7 5.9c.9 2.1 2.5 3.7 4.6 4.6l1.1-1.1c.4-.4 1-.4 1.4 0l2.2 2.2c.4.4.4 1 0 1.4l-1.3 1.3c-.6.6-1.5.8-2.3.5C5.9 13.2 2.8 10.1 1.2 5.6.9 4.8 1.1 3.9 1.7 3.3L3 2c.2-.5.4-.8.6-.8z"/></svg>
        027 815 0937
      </li>
      <li class="contact__item">
        <svg class="contact__icon" viewBox="0 0 16 16" aria-hidden="true"><rect x="1" y="3" width="14" height="10" rx="1" fill="#0f72bd"/><path d="M1.5 4 8 9l6.5-5" fill="none" stroke="#fff" stroke-width="1.2"/></svg>
        warwick@harbourlinepipeworks.example
      </li>
      <li class="contact__item">
        <svg class="contact__icon" viewBox="0 0 16 16" aria-hidden="true"><circle cx="8" cy="8" r="7" fill="#0f72bd"/><path d="M1 8h14M8 1c2.2 2 2.2 12 0 14M8 1c-2.2 2-2.2 12 0 14" fill="none" stroke="#fff" stroke-width="1"/></svg>
        harbourlinepipeworks.example
      </li>
    </ul>

    <div class="person">
      <p class="person__name">Warwick Tane</p>
      <p class="person__role">Director</p>
    </div>
  </section>

  <section class="card card--back" aria-label="Business card back">
    <div class="brand"><span class="brand__dot"></span>Harbourline Pipeworks</div>
    <p class="web">www.harbourlinepipeworks.example</p>
  </section>
</body>
</html>
```